Website Redesign for an Appointment Setting and Lead Generation Company.

I need to redesign an existing website. The website that we are looking to be redesigned is www.trellisvane.example. TrellisVane is a B2B appointment setting organization. The idea is to present a modern look website for professional services company. The idea is to engage the user, look at various services and generate more inbound leads for the website

Target Market(s)

US, APAC, Europe, UK. Focused on B2B companies more than $100 Mn

Industry/Entity Type

Professional Service

Number of Pages Required

5+ page

Font styles to use
Other font styles liked:
• Roboto

Requirements
Must have
• Home Page - Banner Image, Section for Client testimonials
Industry Page - To show industry capabilities
Services Page - To show service capabilities
Blogs Page - to show blogs
Offerings Page - Offerings Page
Nice to have
• I would like to have a elegant design with small animation. Preferably use colors from the logo attached. Use infographics where possible

```html
<!DOCTYPE html>
<html lang="en">
<head>
<meta charset="utf-8">
<title>TrellisVane — Appointment Setting</title>
<link href="https://fonts.googleapis.com/css2?family=Poppins:ital,wght@0,300;0,400;0,500;0,600;0,700;0,800;1,300;1,400&family=Roboto:wght@400;500&display=swap" rel="stylesheet">
<style>
:root{
  --red:#d13a3a;
  --red-dark:#b52f2f;
  --ink:#1d1d1d;
  --text:#444;
  --muted:#777;
  --dark:#242424;
  --darker:#1a1a1a;
  --light:#f4f4f4;
  --white:#fff;
}
*{margin:0;padding:0;box-sizing:border-box}
html,body{width:1200px;height:5164px;overflow:hidden}
body{position:relative;font-family:"Poppins",sans-serif;color:var(--text);background:var(--white)}
.abs{position:absolute}
.btn{position:absolute;background:var(--red);color:var(--white);font:600 12px/1 "Poppins",sans-serif;display:flex;align-items:center;justify-content:center;letter-spacing:.3px;text-transform:uppercase}

/* hero */
.hero{left:0;top:0;width:1200px;height:690px;background:linear-gradient(135deg,#6d7785 0%,#9aa4ae 35%,#c8c2b8 60%,#7d7468 100%)}
.hero-shade{left:0;top:0;width:1200px;height:690px;background:rgba(20,24,30,.35)}
.navbar{left:62px;top:0;width:998px;height:88px;background:var(--white);box-shadow:0 2px 10px rgba(0,0,0,.08)}
.brand{display:flex;align-items:center;gap:8px;font:700 25px/1 "Poppins",sans-serif;color:var(--red)}
.brand-mark{width:18px;height:18px;background:var(--red);border-radius:50%}
.nav-links{right:70px;top:36px;display:flex;gap:26px;font:500 12px/16px "Poppins",sans-serif;color:var(--ink)}
.nav-links .active{color:var(--red)}
.search{left:1060px;top:0;width:76px;height:88px;background:var(--red);display:flex;align-items:center;justify-content:center}
.hero-title{left:0;width:1200px;top:292px;text-align:center;font:800 66px/1 "Poppins",sans-serif;color:var(--white);letter-spacing:1px}
.hero-sub{left:0;width:1200px;top:426px;text-align:center;font:300 27px/1 "Poppins",sans-serif;color:var(--white);letter-spacing:5px}

/* feature cards */
.card{background:var(--white);box-shadow:0 4px 22px rgba(0,0,0,.08);text-align:center}
.card.featured{background:var(--red);color:var(--white)}
.icon-circle{position:absolute;left:50%;margin-left:-60px;width:120px;height:120px;border-radius:50%;background:var(--red);display:flex;align-items:center;justify-content:center}
.featured .icon-circle{background:var(--white)}
.card h3{position:absolute;left:0;width:100%;font:500 20px/1 "Poppins",sans-serif;color:var(--ink)}
.featured h3{color:var(--white)}
.card p{position:absolute;left:38px;right:38px;font:400 13px/25px "Poppins",sans-serif;color:var(--text)}
.featured p{color:var(--white);left:56px;right:56px}

/* section heads */
.eyebrow{font:400 20px/1 "Poppins",sans-serif;color:var(--red)}
.h2{font:700 35px/1 "Poppins",sans-serif;color:var(--ink)}
.body-copy{font:400 13px/26px "Poppins",sans-serif;color:var(--text)}

.photo{background:linear-gradient(180deg,#f1f1f1,#c9ccd2 55%,#3a3f4a)}

/* stats */
.stats{left:0;top:1818px;width:1200px;height:258px;background:linear-gradient(180deg,#2b2b2b,#1f1f1f)}
.stat{position:absolute;top:66px;width:240px;margin-left:-120px;text-align:center}
.stat b{display:block;font:800 70px/1 "Poppins",sans-serif;color:var(--red);letter-spacing:2px}
.stat span{display:block;margin-top:22px;font:400 13px/1 "Poppins",sans-serif;color:var(--white)}

/* progress */
.bar{position:absolute;left:86px;width:448px;height:18px;border-radius:9px;background:#ddd}
.bar i{display:block;height:100%;border-radius:9px;background:repeating-linear-gradient(135deg,#c83232 0 8px,#d94545 8px 16px)}
.bar-label{position:absolute;left:88px;font:500 9.5px/1 "Poppins",sans-serif;color:var(--ink)}
.bubble{position:absolute;width:44px;height:44px;margin-left:-22px;border-radius:50%;background:var(--red);border:3px solid #f1c9c9;color:var(--white);font:600 11px/38px "Poppins",sans-serif;text-align:center}
.bubble::after{content:"";position:absolute;left:50%;bottom:-11px;margin-left:-5px;border:5px solid transparent;border-top:6px solid var(--red)}

/* team */
.member-name{position:absolute;width:300px;text-align:center;font:500 20px/1 "Poppins",sans-serif;color:var(--ink)}
.member-role{position:absolute;width:300px;text-align:center;font:400 13px/1 "Poppins",sans-serif;color:var(--red)}

/* testimonial */
.testimonial{left:0;top:3596px;width:1200px;height:358px;background:linear-gradient(180deg,#cf3b3b,#c53434)}
.avatar{left:108px;top:3692px;width:164px;height:164px;border-radius:50%;border:5px solid var(--white);background:linear-gradient(160deg,#d9dde2,#7f8793)}
.quote{left:326px;top:3702px;width:790px;font:italic 300 22px/31px "Poppins",sans-serif;color:var(--white)}
.quote-name{left:326px;top:3838px;font:500 20px/1 "Poppins",sans-serif;color:var(--white)}
.quote-name small{font:400 13px/1 "Poppins",sans-serif;margin-left:8px}

/* ranking */
.rank-img{position:absolute;top:4232px;width:302px;height:212px}
.rank-tag{position:absolute;top:4406px;height:38px;padding:0 18px;background:var(--red);color:var(--white);font:400 13px/38px "Poppins",sans-serif}
.rank-list{position:absolute;top:4472px;width:300px;font:400 13px/26px "Poppins",sans-serif;color:var(--ink)}
.read-more{position:absolute;top:4590px;width:270px;display:flex;justify-content:space-between;font:400 13px/1 "Poppins",sans-serif;color:var(--red)}

/* footer */
.footer{left:0;top:4726px;width:1200px;height:356px;background:var(--dark)}
.footer-bottom{left:0;top:5082px;width:1200px;height:82px;background:var(--darker);text-align:center;font:400 12px/82px "Poppins",sans-serif;color:#777}
.foot-col h4{font:600 13px/1 "Poppins",sans-serif;color:var(--white);margin-bottom:24px}
.foot-col li{list-style:none;font:400 13px/20.4px "Poppins",sans-serif;color:#aaa;padding-left:16px;position:relative}
.foot-col li::before{content:"✓";position:absolute;left:0;font-size:10px;color:#aaa}
.social{position:absolute;top:4926px;width:20px;height:20px;border-radius:50%;background:#555}
</style>
</head>
<body>

<!-- hero -->
<div class="abs hero" role="img" aria-label="Business people in suits applauding at a conference"></div>
<div class="abs hero-shade"></div>
<header class="abs navbar">
  <div class="abs brand" style="left:30px;top:28px"><span class="brand-mark"></span>TrellisVane</div>
  <nav class="abs nav-links"><span class="active">Home</span><span>Industry</span><span>Services</span><span>Blog</span><span>Offerings</span><span>Contact Us</span></nav>
</header>
<div class="abs search"><svg width="20" height="20" viewBox="0 0 20 20" fill="none" stroke="#fff" stroke-width="2"><circle cx="8.5" cy="8.5" r="6"/><path d="M13 13l5 5"/></svg></div>
<h1 class="abs hero-title">APPOINTMENT SETTING</h1>
<div class="abs hero-sub">Lead Generation</div>
<a class="btn" style="left:524px;top:502px;width:142px;height:52px">Know More</a>

<!-- feature cards -->
<div class="abs card" style="left:140px;top:824px;width:290px;height:326px">
  <div class="icon-circle" style="top:34px"><svg width="56" height="56" viewBox="0 0 56 56" fill="none" stroke="#fff" stroke-width="2.5"><rect x="8" y="12" width="40" height="36" rx="3"/><path d="M8 22h40M18 6v10M38 6v10"/><path d="M16 30h6M26 30h6M36 30h6M16 38h6M26 38h6"/></svg></div>
  <h3 style="top:208px">Global Partner</h3>
  <p style="top:248px">With Delivery locations across 4 countries, TrellisVane</p>
</div>
<div class="abs card featured" style="left:434px;top:802px;width:328px;height:364px">
  <div class="icon-circle" style="top:54px"><svg width="56" height="56" viewBox="0 0 56 56" fill="none" stroke="#d13a3a" stroke-width="2.5"><rect x="12" y="10" width="32" height="40" rx="3"/><rect x="21" y="6" width="14" height="8" rx="2"/><path d="M19 24h18M19 32h18M19 40h10"/></svg></div>
  <h3 style="top:230px">Domain Expertise</h3>
  <p style="top:270px">15,000+ campaigns executed across 12 verticals</p>
</div>
<div class="abs card" style="left:770px;top:824px;width:282px;height:326px">
  <div class="icon-circle" style="top:34px"><svg width="56" height="56" viewBox="0 0 56 56" fill="none" stroke="#fff" stroke-width="2.5"><path d="M14 6h20l10 10v34H14z"/><path d="M34 6v10h10"/><path d="M20 26h18M20 33h18M20 40h18"/></svg></div>
  <h3 style="top:208px">Proprietary</h3>
  <p style="top:248px">Our unique &amp; proprietary Call CLEAR Model, powered</p>
</div>

<!-- dynamic solutions -->
<div class="abs eyebrow" style="left:144px;top:1294px">Niche Product Offerings</div>
<h2 class="abs h2" style="left:144px;top:1334px">DYNAMIC SOLUTIONS</h2>
<p class="abs body-copy" style="left:146px;top:1388px;width:440px">We are a leading B2B lead generation company with presence across North America, Europe, APAC and India. Our experienced and trained lead generation executives understand your unique service offerings and work along your campaign journey to achieve the desired goals.</p>
<p class="abs body-copy" style="left:146px;top:1540px;width:440px">Leveraging our extensive proprietary database, we target key decision-makers &amp; influencers across industries.</p>
<a class="btn" style="left:144px;top:1640px;width:142px;height:54px">View More</a>
<div class="abs photo" style="left:630px;top:1196px;width:450px;height:622px;background:linear-gradient(180deg,#fff 0%,#eef0f3 30%,#5a606c 60%,#2c3038 100%)" role="img" aria-label="Four business professionals standing with arms crossed"></div>

<!-- stats -->
<section class="abs stats">
  <div class="stat" style="left:210px"><b>45 %</b><span>North America</span></div>
  <div class="stat" style="left:460px"><b>35 %</b><span>UK/EMEA</span></div>
  <div class="stat" style="left:724px"><b>15 %</b><span>APAC &amp; ANZ</span></div>
  <div class="stat" style="left:1020px"><b>5 %</b><span>Rest of the World</span></div>
</section>

<!-- capabilities -->
<div class="bubble" style="left:204px;top:2206px">22%</div>
<div class="bar" style="top:2270px"><i style="width:27%"></i></div>
<div class="bar-label" style="top:2298px">Multilingual Campaigns Executed by Onsite Resources</div>
<div class="bubble" style="left:266px;top:2332px">35%</div>
<div class="bar" style="top:2396px"><i style="width:41%"></i></div>
<div class="bar-label" style="top:2424px">Campaigns on Traditional IT &amp; Infrastructure Management Services</div>
<div class="bubble" style="left:346px;top:2456px">65%</div>
<div class="bar" style="top:2520px"><i style="width:59%"></i></div>
<div class="bar-label" style="top:2548px">Campaigns on AI/ML/RPA, Product Engineering &amp; Digital Transformation</div>
<div class="bubble" style="left:224px;top:2586px">25%</div>
<div class="bar" style="top:2650px"><i style="width:31%"></i></div>
<div class="bar-label" style="top:2680px">Campaigns on Events Audience Acquisition</div>

<div class="abs eyebrow" style="left:624px;top:2268px">For Competitive Offerings</div>
<h2 class="abs h2" style="left:624px;top:2308px">LEADING-EDGE CAPABILITIES</h2>
<p class="abs body-copy" style="left:626px;top:2362px;width:450px">As the needs of your clients evolve, so should your service offerings. Our capabilities boost your sales pipeline for global outreach and give you an edge over your competitors.</p>
<p class="abs body-copy" style="left:626px;top:2464px;width:450px">To understand your prospects' needs and your service offerings, TrellisVane' executives are regularly trained on domains and next-generation service offerings. Our capabilities include delivering campaigns in local languages across continents &amp;</p>
<a class="btn" style="left:632px;top:2614px;width:142px;height:54px">View More</a>

<!-- team -->
<div class="abs eyebrow" style="left:0;width:1232px;top:2842px;text-align:center">Our Experts</div>
<h2 class="abs h2" style="left:0;width:1232px;top:2878px;text-align:center">Meet Our Team</h2>
<p class="abs body-copy" style="left:360px;top:2936px;width:512px;text-align:center">Einim veniam quis nostrud exercitation ullamco laboris nisi ut sed aliquip consequat. Duis aute irure ipsum dolorn reprehend</p>
<div class="abs photo" style="left:134px;top:3036px;width:296px;height:404px;background:linear-gradient(180deg,#b7c2cc,#6f7985)" role="img" aria-label="Portrait of a smiling team member with glasses"></div>
<div class="abs photo" style="left:462px;top:3036px;width:298px;height:404px;background:linear-gradient(180deg,#e4e2de,#b9ae9c)" role="img" aria-label="Portrait of a smiling consultant"></div>
<div class="abs" style="left:682px;top:3066px;width:50px;height:50px;border-radius:50%;background:var(--red);display:flex;align-items:center;justify-content:center"><svg width="18" height="18" viewBox="0 0 20 20" fill="none" stroke="#fff" stroke-width="2"><circle cx="8.5" cy="8.5" r="6"/><path d="M13 13l5 5"/></svg></div>
<div class="abs photo" style="left:786px;top:3036px;width:296px;height:404px;background:linear-gradient(180deg,#dfe6ee,#4c5260)" role="img" aria-label="Portrait of a smiling manager in a suit"></div>
<div class="member-name" style="left:144px;top:3462px">Owen Harlow</div>
<div class="member-role" style="left:144px;top:3490px">IT Person</div>
<div class="member-name" style="left:468px;top:3462px">Clara Brenn</div>
<div class="member-role" style="left:468px;top:3490px">Consultant</div>
<div class="member-name" style="left:788px;top:3462px">Owen Harlow</div>
<div class="member-role" style="left:788px;top:3490px">Manager</div>

<!-- testimonial -->
<section class="abs testimonial"></section>
<div class="abs avatar" role="img" aria-label="Portrait of the client giving the testimonial"></div>
<p class="abs quote">Lorem ipsum dolor sit amet, consectetur adipiscing elit. Vestibulum augue leo, convallis in nisi vel, rhoncus lacinia quam. Nullam lorem orci, suscipit non tempus eget, euismod in arcu.</p>
<div class="abs quote-name">Owen Harlow <small>- chief Marketing Officer</small></div>
<svg class="abs" style="left:784px;top:3842px" width="56" height="16" viewBox="0 0 56 16" fill="none" stroke="#fff" stroke-width="2"><path d="M11 3l-5 5 5 5M45 3l5 5-5 5"/></svg>
<svg class="abs" style="left:1020px;top:3822px" width="66" height="52" viewBox="0 0 66 52" fill="#fff"><path d="M2 2h26v26c0 12-8 22-20 24l-2-8c6-2 9-6 9-12H2z"/><path d="M36 2h26v26c0 12-8 22-20 24l-2-8c6-2 9-6 9-12H36z"/></svg>

<!-- ranking -->
<h2 class="abs h2" style="left:0;width:1176px;top:4090px;text-align:center">OUR RANKING</h2>
<div class="abs eyebrow" style="left:0;width:1176px;top:4142px;text-align:center">Ranked amongst the top B2B Lead Generation Companies</div>

<div class="rank-img" style="left:98px;background:linear-gradient(180deg,#6c7fa6,#b98a6c 55%,#5a4a55)" role="img" aria-label="City skyline at dusk in North America"></div>
<div class="rank-tag" style="left:98px">North America</div>
<div class="rank-list" style="left:116px">Delivery Centre in California<br>Multiple Sales Offices Across US<br>CAN-SPAM Compliant Process<br>End-to-End Event Execution</div>
<div class="read-more" style="left:116px"><span>READ MORE</span><span>→</span></div>

<div class="rank-img" style="left:442px;background:linear-gradient(180deg,#8eb5e0,#c9d4de 50%,#7d6a5a)" role="img" aria-label="Clock tower and customs sign in the UK"></div>
<div class="rank-tag" style="left:442px">Europe &amp; UK</div>
<div class="rank-list" style="left:462px">Delivery Centre in UK &amp; Germany<br>Multilingual Lead Generation<br>Capabilities in 20+ Languages<br>GDPR Compliant ProcessCapabilities</div>
<div class="read-more" style="left:462px"><span>READ MORE</span><span>→</span></div>

<div class="rank-img" style="left:788px;background:linear-gradient(180deg,#c9ccd0,#9a9590 50%,#6b6660)" role="img" aria-label="Busy city street with traffic in India"></div>
<div class="rank-tag" style="left:788px">APAC</div>
<div class="rank-list" style="left:810px">Delivery Centre in India<br>Extensive Database of Decision Makers<br>CAN-SPAM Compliant Process</div>
<div class="read-more" style="left:810px"><span>READ MORE</span><span>→</span></div>

<!-- footer -->
<footer class="abs footer"></footer>
<div class="abs foot-col" style="left:98px;top:4798px"><h4>ABOUT US</h4><ul><li>About</li><li>Our Team</li><li>Awards</li><li>Our Partnerships</li><li>Our Differentiators</li><li>Locations</li></ul></div>
<div class="abs foot-col" style="left:306px;top:4798px"><h4>SERVICES</h4><ul><li>B2B Appointment Setting</li><li>Account Based Marketing</li><li>Research As A Service</li><li>Event Audience Acquisition</li><li>Staffing &amp; Talent Acquisition</li><li>Digital Marketing</li><li>Social Media Research</li><li>Lead Nurturing</li></ul></div>
<div class="abs foot-col" style="left:570px;top:4798px"><h4>LIBRARY</h4><ul><li>Videos</li><li>Infographics</li><li>Blog</li><li>Case Studies</li></ul></div>
<div class="abs brand" style="left:806px;top:4846px;font-size:32px"><span class="brand-mark" style="width:22px;height:22px"></span>TrellisVane</div>
<span class="social" style="left:862px" aria-label="Social link"></span>
<span class="social" style="left:922px" aria-label="Social link"></span>
<span class="social" style="left:980px" aria-label="Social link"></span>
<div class="abs footer-bottom">Privacy Policy | Copyright All Rights Reserved © 2020</div>

</body>
</html>
```